Redesign Company Website WRAPTIDE

We want to redesign the web page of the company using some actual pictures such as the ones that show the production line, equipment and the plant. About the products picture i am ok if upgrade for new ones o keep some of them.
PLease visiti: www.lumodiseno.example.ve/wraptide/ to check the actual page.

Target Market(s)

Processors and Producers of:
Cheese, Fresh Meat, Sausages, Poultry, Processed Meats,

Coding

Coded - Design and coding required

Number of Pages Required

5+ page

Requirements
Must have
• Bilingual Spanish/English
Nice to have

Should not have
• Blogs, or any customer interaction, no particular brand must be shown, must be all generic.

```html
<!DOCTYPE html>
<html lang="es">
<head>
<meta charset="utf-8">
<title>Wraptide – Soluciones de embalaje flexibles</title>
<link href="https://fonts.googleapis.com/css2?family=Open+Sans:wght@400;600;700&display=swap" rel="stylesheet">
<style>
  :root {
    --ink: #000000;
    --paper: #ffffff;
    --green: #8dc63f;
    --teal: #13a58f;
    --muted: #8a8a8a;
    --nav-dark: #1a1a1a;
  }
  * { margin: 0; padding: 0; box-sizing: border-box; }
  html, body { width: 1200px; height: 682px; overflow: hidden; }
  body {
    background: var(--ink);
    font-family: "Open Sans", Arial, sans-serif;
    position: relative;
  }
  .topbar {
    position: absolute; left: 0; top: 0;
    width: 1200px; height: 33px;
    background: var(--paper);
  }
  .main-nav {
    position: absolute; left: 485px; top: 8px;
    display: flex; gap: 18px;
    font-size: 12.5px; font-weight: 600;
  }
  .main-nav a { text-decoration: none; color: var(--teal); }
  .main-nav a.is-current { color: var(--nav-dark); }
  .main-nav a.is-hover { color: var(--green); }
  .brand-tab {
    position: absolute; left: 165px; top: 0;
    width: 198px; height: 114px;
    background: var(--paper);
    border-bottom-right-radius: 22px;
    display: flex; align-items: center; justify-content: center;
  }
  .brand-name {
    font-size: 26px; font-weight: 700; letter-spacing: 1px;
    color: var(--teal);
  }
  .hero-title {
    position: absolute; left: 165px; top: 218px;
    font-size: 42px; line-height: 44px;
    color: var(--paper); font-weight: 400;
  }
  .hero-title strong { display: block; color: var(--green); font-weight: 700; letter-spacing: 0.5px; }
  .hero-visual {
    position: absolute; left: 650px; top: 88px;
    width: 382px; height: 390px;
    background: radial-gradient(ellipse at 45% 40%, #cfc40e 0%, #b7ae0c 38%, #8a8410 60%, #c9c9c9 82%, #e8e8e8 100%);
    clip-path: polygon(0 0, 356px 0, 356px 241px, 382px 241px, 382px 390px, 228px 390px, 228px 316px, 0 316px);
  }
  .intro {
    position: absolute; left: 165px; top: 447px;
    font-size: 12.3px; line-height: 17px;
    color: var(--paper); text-transform: uppercase;
  }
  .intro em { font-style: normal; color: var(--teal); }
  .btn-more {
    position: absolute; left: 165px; top: 522px;
    width: 171px; height: 39px;
    background: var(--paper); color: var(--nav-dark);
    border-radius: 3px;
    display: flex; align-items: center; justify-content: center;
    font-size: 16px; text-decoration: none;
  }
  .site-footer {
    position: absolute; left: 165px; top: 661px;
    font-size: 10.5px; color: var(--muted);
  }
</style>
</head>
<body>
  <header class="topbar">
    <nav class="main-nav">
      <a href="#" class="is-current">Home</a>
      <a href="#" class="is-hover">Nosotros</a>
      <a href="#">Mercados</a>
      <a href="#">Empaques</a>
      <a href="#">Interes</a>
      <a href="#">Contacto</a>
    </nav>
  </header>

  <div class="brand-tab"><span class="brand-name">WRAPTIDE</span></div>

  <h1 class="hero-title">SOLUCIONES DE<strong>EMBALAJE FLEXIBLES</strong></h1>

  <div class="hero-visual" role="img" aria-label="Bolsas flexibles tipo doypack en amarillo, blanco, verde y rojo junto a rollos de película transparente"></div>

  <p class="intro">Somos una empresa <em>convertidora de empaques flexibles, originaria</em> de Maracaibo, Venezuela,<br><em>con 30 años de experiencia</em> en el mercado.</p>

  <a href="#" class="btn-more">VIEW MORE</a>

  <footer class="site-footer">© 2020 Wraptide. Todos los derechos reservados</footer>
</body>
</html>
```